Design for Chirpwall Ad to promote Laptops purchase

Need a graphic design for a Chirpwall Ad - to promote 2 laptops (PC and Zorvane) with the stated required ad-text.

AD TEXT:

FOR SME BUSINESS ONLY!
Chat with us!
To get advice on how to apply
and defray up to 80%* of business laptop purchase cost!

*Terms and Conditions apply

Image for reference only

Target Market(s)

Small medium business

Font styles to use
Sans Serif

Requirements
Must have
• 2 laptop images (see attached ) - 1 vector image of ZORVANE , and pls try to create another vector image of PC laptop (where screen is showing Blue Pendrel screen)

```html
<!DOCTYPE html>
<html lang="en">
<head>
<meta charset="utf-8">
<title>SME Business Laptop Offer</title>
<link rel="stylesheet" href="https://fonts.googleapis.com/css2?family=Barlow+Condensed:wght@600;700;800&family=Barlow+Semi+Condensed:wght@600&display=swap">
<style>
  :root {
    --frame: #000000;
    --paper: #ffffff;
    --navy: #27399a;
    --red: #e31e24;
    --ink: #0b0b0b;
    --blue-deep: #2f4fae;
    --blue-mid: #3a7bc8;
    --blue-light: #5aaee0;
    --teal: #58c0d6;
  }
  * { margin: 0; padding: 0; box-sizing: border-box; }
  html, body { width: 1200px; height: 1200px; overflow: hidden; background: var(--frame); }
  .canvas { position: relative; width: 1200px; height: 1200px; background: var(--frame); }
  .ad {
    position: absolute; left: 86px; top: 86px; width: 1028px; height: 1028px;
    background: var(--paper); overflow: hidden;
  }
  .ad__backdrop { position: absolute; inset: 0; width: 100%; height: 100%; }
  .headline {
    position: absolute; left: 64px; font-family: "Barlow Condensed", sans-serif;
    color: var(--navy); font-weight: 700; line-height: 1; white-space: nowrap;
  }
  .headline--sme { top: 62px; font-size: 112px; letter-spacing: 1px; }
  .headline--business { top: 160px; font-size: 86px; }
  .cta {
    position: absolute; left: 60px; top: 232px;
    font-family: "Barlow Condensed", sans-serif; font-weight: 800;
    font-size: 172px; line-height: 1; color: var(--red); white-space: nowrap;
    letter-spacing: 1px;
    -webkit-text-stroke: 0;
    text-shadow:
      -3px -3px 0 #fff, 3px -3px 0 #fff, -3px 3px 0 #fff, 3px 3px 0 #fff,
      0 -4px 0 #fff, 0 4px 0 #fff, -4px 0 0 #fff, 4px 0 0 #fff,
      6px 8px 10px rgba(0,0,0,0.45);
  }
  .offer {
    position: absolute; left: 62px; top: 404px;
    font-family: "Barlow Semi Condensed", sans-serif; font-weight: 600;
    font-size: 42px; line-height: 52px; color: var(--ink); white-space: nowrap;
    letter-spacing: -0.3px;
  }
  .device { position: absolute; }
  .device--left {
    left: 42px; top: 538px; width: 496px; height: 320px;
    border-radius: 14px 14px 8px 8px;
    background: linear-gradient(180deg, #2b2b2b 0%, #e8a5b8 25%, #d9577f 45%, #2d5a90 62%, #c9c9c9 66%, #8d8d8d 85%, #d8d8d8 100%);
  }
  .device--right {
    left: 330px; top: 602px; width: 656px; height: 332px;
    border-radius: 28px 28px 10px 10px;
    background: linear-gradient(160deg, #9aa0a6 0%, #0e1a36 10%, #113a7a 50%, #2f8fe0 70%, #0b1a3a 86%, #c7cbd0 92%, #6b6f75 100%);
  }
  .terms {
    position: absolute; left: 782px; top: 983px;
    font-family: "Barlow Condensed", sans-serif; font-weight: 600;
    font-size: 15px; color: #ffffff; white-space: nowrap;
  }
</style>
</head>
<body>
<div class="canvas">
  <div class="ad">
    <svg class="ad__backdrop" viewBox="0 0 1028 1028" preserveAspectRatio="none" aria-hidden="true">
      <defs>
        <linearGradient id="blueField" x1="0" y1="0" x2="1" y2="1">
          <stop offset="0" stop-color="var(--blue-mid)"/>
          <stop offset="0.55" stop-color="var(--blue-deep)"/>
          <stop offset="1" stop-color="var(--blue-mid)"/>
        </linearGradient>
        <linearGradient id="tealSweep" x1="0" y1="1" x2="1" y2="0">
          <stop offset="0" stop-color="var(--teal)"/>
          <stop offset="1" stop-color="var(--blue-light)" stop-opacity="0.4"/>
        </linearGradient>
      </defs>
      <path d="M362,0 C560,120 700,360 620,600 C540,830 260,970 0,1028 L1028,1028 L1028,0 Z" fill="url(#blueField)"/>
      <path d="M620,0 C780,160 860,420 800,640 C740,860 520,980 300,1028 L1028,1028 L1028,0 Z" fill="#2b44a5" opacity="0.45"/>
      <path d="M840,0 C940,200 1000,420 1028,560 L1028,0 Z" fill="var(--blue-light)" opacity="0.35"/>
      <path d="M60,1028 C300,900 520,860 720,900 C860,930 960,980 1028,1028 Z" fill="url(#tealSweep)" opacity="0.6"/>
      <path d="M0,1028 C40,1010 80,1000 120,994 L140,1028 Z" fill="#7a6fc0" opacity="0.7"/>
    </svg>

    <div class="headline headline--sme">FOR SME</div>
    <div class="headline headline--business">Business Only!</div>
    <div class="cta">CHAT WITH US!</div>
    <p class="offer">To get advice on how to apply and defray up to 80%*<br>of business laptop purchase cost!</p>

    <div class="device device--left" role="img" aria-label="Illustration of a silver Zorvane laptop with a pink and blue gradient screen"></div>
    <div class="device device--right" role="img" aria-label="Illustration of a PC laptop showing a blue Pendrel start screen"></div>

    <div class="terms">*Terms and Conditions apply</div>
  </div>
</div>
</body>
</html>
```